New Business Card Design Project

New business card design required for an electrical business in Australia. Offering quality electrical services including design and installation. Electrical services offered are domestic, commercial and industrial. Also meets all the air conditioning installation and maintenance needs.

Target Market(s)

The business is sleek, professional and caters primarily to wealthy clients and government contracts looking for exceptional, tailored service.

Industry/Entity Type

Electrical

Contact Information for Business Card

Damian Corlowe (Director)
0438 615 274
admin@vrtelectrical.com.au
www.vrtelectrical.com.au

Font styles to use
Sans Serif

Requirements
Must have
• The business card must show the license number - 64193 to comply with legislation.
Nice to have
• The logo colours and fonts could be incorporated into the design if the designer sees fit. We are open to new ideas and welcome creativity. The logo style guide is attached for reference if required.

```html
<!DOCTYPE html>
<html lang="en">
<head>
<meta charset="utf-8">
<title>VRT Electrical – Business Card</title>
<link href="https://fonts.googleapis.com/css2?family=Montserrat:wght@400;500;800&family=Open+Sans:wght@400&family=Poppins:wght@300;400;500&display=swap" rel="stylesheet">
<style>
  :root {
    --navy: #162c5a;
    --navy-deep: #111c3c;
    --white: #ffffff;
    --stage: #e9e6e1;
    --ink: #1c2233;
    --rule: #1f3468;
  }
  * { box-sizing: border-box; margin: 0; padding: 0; }
  html, body { width: 1200px; height: 1089px; overflow: hidden; }
  body { background: var(--white); font-family: "Poppins", sans-serif; position: relative; }

  .sheet-header { height: 175px; text-align: center; color: var(--navy); padding-top: 42px; }
  .sheet-title { font-family: "Montserrat", sans-serif; font-size: 52px; line-height: 1; }
  .sheet-title strong { font-weight: 800; letter-spacing: 1px; }
  .sheet-title span { font-family: "Open Sans", sans-serif; font-weight: 400; }
  .sheet-size { font-family: "Open Sans", sans-serif; font-size: 32px; margin-top: 8px; }

  .stage { position: absolute; top: 175px; left: 0; width: 1200px; height: 914px; background: var(--stage); }

  .card {
    position: absolute; width: 560px; height: 345px; overflow: hidden;
    box-shadow: 0 18px 36px rgba(0,0,0,.25);
  }
  .card--front { left: 60px; top: 90px; background: var(--white); display: flex; }
  .card--back { left: 580px; top: 490px; background: radial-gradient(circle at 55% 40%, #1e2b57, var(--navy-deep) 75%); color: var(--white); }

  .front-brand {
    width: 240px; flex: none; background: var(--navy);
    display: flex; align-items: center; justify-content: center;
    padding: 0 28px;
  }
  .brand-name {
    color: var(--white); font-family: "Poppins", sans-serif; font-weight: 400;
    font-size: 24px; line-height: 1.45; letter-spacing: 3px; text-align: center;
  }
  .brand-name span { display: block; }

  .front-details { flex: 1; padding: 52px 36px 0 40px; color: var(--ink); }
  .person-name { font-size: 26px; font-weight: 400; color: var(--ink); white-space: nowrap; }
  .person-rule { display: flex; align-items: center; gap: 10px; margin-top: 4px; }
  .person-role { font-size: 12px; color: var(--navy); }
  .person-rule::after { content: ""; flex: 1; height: 1.5px; background: var(--rule); }

  .contact-list { list-style: none; margin-top: 78px; }
  .contact-list li { display: flex; align-items: center; gap: 9px; font-size: 13px; color: var(--ink); margin-bottom: 9px; white-space: nowrap; }
  .contact-icon { width: 18px; height: 18px; flex: none; }

  .back-brand { position: absolute; left: 0; right: 0; top: 120px; text-align: center; font-size: 40px; letter-spacing: 6px; }
  .license { position: absolute; left: 0; right: 0; bottom: 58px; text-align: center; font-family: "Montserrat", sans-serif; font-weight: 400; font-size: 14px; letter-spacing: 5px; }
</style>
</head>
<body>
  <header class="sheet-header">
    <h1 class="sheet-title"><strong>BUSINESS CARD</strong><span>- Mockup1</span></h1>
    <p class="sheet-size">Size: 3.25 in X 2.00 IN</p>
  </header>

  <main class="stage">
    <section class="card card--front" aria-label="Card front">
      <div class="front-brand">
        <p class="brand-name"><span>VRT</span><span>ELECTRICAL</span></p>
      </div>
      <div class="front-details">
        <h2 class="person-name">Damian Corlowe</h2>
        <div class="person-rule"><span class="person-role">Director</span></div>
        <ul class="contact-list">
          <li>
            <svg class="contact-icon" viewBox="0 0 20 20" aria-hidden="true"><circle cx="10" cy="10" r="8.5" fill="none" stroke="#162c5a" stroke-width="1.6"/><path d="M7 6.5c0 4 2.5 6.5 6.5 6.5l.5-1.8-2-1-1 1c-1-.5-1.8-1.3-2.2-2.2l1-1-1-2z" fill="#162c5a"/></svg>
            0438 615 274
          </li>
          <li>
            <svg class="contact-icon" viewBox="0 0 20 20" aria-hidden="true"><circle cx="10" cy="10" r="8.5" fill="none" stroke="#162c5a" stroke-width="1.6"/><rect x="6" y="7" width="8" height="6" rx="1" fill="#162c5a"/></svg>
            admin@vrtelectrical.com.au
          </li>
          <li>
            <svg class="contact-icon" viewBox="0 0 20 20" aria-hidden="true"><circle cx="10" cy="10" r="8.5" fill="none" stroke="#162c5a" stroke-width="1.6"/><circle cx="10" cy="10" r="4" fill="#162c5a"/></svg>
            www.vrtelectrical.com.au
          </li>
        </ul>
      </div>
    </section>

    <section class="card card--back" aria-label="Card back">
      <p class="back-brand">VRT ELECTRICAL</p>
      <p class="license">LICENSE NUMBER - 64193</p>
    </section>
  </main>
</body>
</html>
```